Ironvale Holdings Business card

We need a an amazing matte black and gold card! W are a finance investing company so we want something that's eye catching and sleek. We want it to be attractive and sleek and represent money. Heck with would like the letters and lgo to be printed as 24k gold one day. We have the logo added so please use the color scheme with the logo and have that beautifully placed on one side.

Target Market(s)

Investors of all ages

Industry/Entity Type

Financial

Contact Information for Business Card

Black and matte with gold lettering follow logo colrs please.

Font styles to use
Other font styles liked:
• you decide

Colors

Designer to choose colors to be used in the design.

Requirements
Must have
• Matte Black and Gold, logo on one side. job title and name , website, phone number and email address on the other side
Nice to have
• Matte black and crisp finish to attract investors
Should not have
• playful, very professional!

```html
<!DOCTYPE html>
<html lang="en">
<head>
<meta charset="utf-8">
<title>Ironvale Holdings Business Card</title>
<link rel="stylesheet" href="https://fonts.googleapis.com/css2?family=Cinzel:wght@400;600&family=Tinos:wght@400;700&display=swap">
<style>
  :root {
    --backdrop: #1c1c1f;
    --card-black: #0d0d0e;
    --gold: #d6b43c;
    --gold-bright: #ecd35a;
    --gold-deep: #a8891f;
    --ink-light: #e8e8e8;
  }
  * { box-sizing: border-box; margin: 0; padding: 0; }
  html, body {
    width: 1200px; height: 800px; overflow: hidden;
    background: var(--backdrop);
  }
  .canvas {
    position: relative; width: 1200px; height: 800px;
  }
  .card {
    position: absolute; width: 525px; height: 300px;
    background: var(--card-black);
    box-shadow: 0 18px 40px rgba(0,0,0,0.55);
    overflow: hidden;
  }
  /* Front side */
  .card-front { left: 70px; top: 110px; }
  .brand {
    position: absolute; left: 0; right: 0; top: 96px;
    text-align: center;
  }
  .brand-name {
    font-family: "Cinzel", serif; font-weight: 600;
    font-size: 38px; letter-spacing: 2px; color: var(--gold);
  }
  .brand-rule {
    width: 340px; height: 1px; margin: 10px auto 0;
    background: var(--gold);
  }
  .front-rule {
    position: absolute; left: 0; right: 0; bottom: 48px;
    height: 1px; background: var(--gold-deep);
  }
  .front-web {
    position: absolute; left: 0; right: 0; bottom: 62px;
    text-align: center;
    font-family: "Tinos", serif; font-size: 12px;
    letter-spacing: 4px; color: var(--gold);
  }
  /* Back side */
  .card-back { left: 605px; top: 390px; }
  .holder {
    position: absolute; left: 0; right: 0; top: 70px; text-align: center;
  }
  .holder-name {
    font-family: "Cinzel", serif; font-weight: 600;
    font-size: 24px; color: var(--gold); letter-spacing: 1px;
  }
  .holder-title {
    font-family: "Tinos", serif; font-size: 12px;
    color: var(--ink-light); letter-spacing: 1px; margin-top: 2px;
  }
  .contact {
    position: absolute; left: 0; right: 0; top: 140px;
    text-align: center;
    font-family: "Tinos", serif; font-size: 13px;
    color: var(--ink-light); line-height: 22px;
  }
  .contact-line { display: flex; justify-content: center; align-items: center; gap: 6px; }
  .contact-web strong { font-weight: 700; }
  .icon { width: 11px; height: 11px; }
  .divider { color: var(--ink-light); padding: 0 2px; }
  .gold-band {
    position: absolute; left: 0; right: 0; bottom: 0; height: 9px;
    background: linear-gradient(90deg, var(--gold-deep), var(--gold-bright), var(--gold));
  }
</style>
</head>
<body>
<main class="canvas">
  <section class="card card-front" aria-label="Card front">
    <div class="brand">
      <div class="brand-name">IRONVALE HOLDINGS</div>
      <div class="brand-rule"></div>
    </div>
    <div class="front-web">www.IRONVALEHOLDINGS.com</div>
    <div class="front-rule"></div>
  </section>

  <section class="card card-back" aria-label="Card back">
    <div class="holder">
      <div class="holder-name">DANIEL HART</div>
      <div class="holder-title">OWNER</div>
    </div>
    <div class="contact">
      <div class="contact-line">
        <svg class="icon" viewBox="0 0 11 11" aria-hidden="true"><rect x="2.5" y="0.8" width="6" height="9.4" rx="1" fill="none" stroke="var(--gold)" stroke-width="1.3"/></svg>
        <span>+61 400 218 736</span>
        <span class="divider">|</span>
        <svg class="icon" viewBox="0 0 11 11" aria-hidden="true"><rect x="0" y="1.5" width="11" height="8" fill="var(--gold)"/><path d="M0.5 2 L5.5 6 L10.5 2" fill="none" stroke="var(--card-black)" stroke-width="1"/></svg>
        <span>info@ironvaleholdings.com</span>
      </div>
      <div class="contact-line contact-web">www.<strong>ironvaleholdings</strong>.com</div>
      <div class="contact-line">PO Box 480, 12 Collins Lane, Melbourne</div>
    </div>
    <div class="gold-band"></div>
  </section>
</main>
</body>
</html>
```